Crestmoor Business Cards

I need a business card designed with the following information.

Company Name: Crestmoor Wealth Management
Name: BriAnne Tolvey
Title: Executive Assistant
Cell: (555) 302-7164
Direct Line: (555) 917-5082
Email: brianne@crestmoorwm.example
Address: 20537 W. Harwell PKWY Ste. B
Larkmere, Nv 77512

I have attached the logo.
I would like it in navy blue and silver.
Thanks.

```html
<!DOCTYPE html>
<html lang="en">
<head>
<meta charset="utf-8">
<title>Crestmoor Wealth Management – Business Cards</title>
<link href="https://fonts.googleapis.com/css2?family=Work+Sans:wght@400;500&display=swap" rel="stylesheet">
<style>
  :root {
    --navy: #13223f;
    --silver: #eef1f5;
    --silver-soft: #c9d0da;
    --backdrop: #e4e6e9;
  }
  * { margin: 0; padding: 0; box-sizing: border-box; }
  html, body { width: 1200px; height: 1000px; overflow: hidden; }
  body {
    background: var(--backdrop);
    font-family: "Work Sans", sans-serif;
    color: var(--silver);
    position: relative;
  }
  .card {
    position: absolute;
    left: 200px;
    width: 800px;
    height: 456px;
    background: var(--navy);
    box-shadow: 0 4px 14px rgba(0,0,0,0.25);
  }
  .card--front { top: 30px; }
  .card--back { top: 516px; }

  .brand {
    position: absolute;
    left: 0; right: 0;
    text-align: center;
    font-weight: 400;
    color: var(--silver);
  }
  .brand__mark {
    display: block;
    margin: 0 auto;
    border: 2px solid var(--silver);
    border-radius: 50%;
  }
  .brand__name { display: block; text-transform: uppercase; }
  .brand__sub { display: block; text-transform: uppercase; }

  .card--front .brand { top: 38px; }
  .card--front .brand__mark { width: 96px; height: 96px; margin-bottom: 26px; }
  .card--front .brand__name { font-size: 27px; letter-spacing: 8px; line-height: 1; }
  .card--front .brand__sub { font-size: 11px; letter-spacing: 3px; margin-top: 10px; }

  .card--back .brand { top: 76px; }
  .card--back .brand__mark { width: 150px; height: 150px; margin-bottom: 40px; }
  .card--back .brand__name { font-size: 38px; letter-spacing: 11px; line-height: 1; }
  .card--back .brand__sub { font-size: 16px; letter-spacing: 4px; margin-top: 16px; }

  .person {
    position: absolute;
    right: 432px;
    top: 280px;
    text-align: right;
  }
  .person__name { font-size: 28px; letter-spacing: 2px; font-weight: 400; text-transform: uppercase; line-height: 1; }
  .person__title { font-size: 17px; letter-spacing: 1px; margin-top: 12px; }

  .divider {
    position: absolute;
    left: 390px; top: 258px;
    width: 2px; height: 100px;
    background: var(--silver);
  }

  .contacts {
    position: absolute;
    left: 418px; top: 263px;
    list-style: none;
    font-size: 17px;
    line-height: 24px;
  }
  .contacts li { display: flex; align-items: center; }
  .contacts svg { width: 12px; height: 12px; margin-right: 12px; fill: none; stroke: var(--silver); stroke-width: 1.6; }

  .rule {
    position: absolute;
    left: 0; right: 0; top: 400px;
    height: 2px;
    background: var(--silver);
  }
  .address {
    position: absolute;
    left: 0; right: 24px; top: 420px;
    text-align: center;
    font-size: 16px;
  }

  .web {
    position: absolute;
    left: 0; right: 0; bottom: 20px;
    text-align: center;
    font-size: 17px;
  }
  .web strong { font-weight: 500; }
</style>
</head>
<body>

<section class="card card--front">
  <div class="brand">
    <span class="brand__mark"></span>
    <span class="brand__name">Crestmoor</span>
    <span class="brand__sub">Wealth Management</span>
  </div>

  <div class="person">
    <p class="person__name">BriAnne Tolvey</p>
    <p class="person__title">Executive Assistant</p>
  </div>

  <div class="divider"></div>

  <ul class="contacts">
    <li>
      <svg viewBox="0 0 12 12"><path d="M2 1.5 L4 1.5 L5 4 L3.8 5 Q5 7.5 7 8.2 L8 7 L10.5 8 L10.5 10 Q6 10.5 3.5 7.5 Q1.5 5 2 1.5 Z"/></svg>
      (555) 302-7164
    </li>
    <li>
      <svg viewBox="0 0 12 12"><rect x="3" y="1" width="6" height="10" rx="1"/><line x1="5" y1="9" x2="7" y2="9"/></svg>
      (555) 917-5082
    </li>
    <li>
      <svg viewBox="0 0 12 12"><rect x="1" y="2.5" width="10" height="7"/><path d="M1 2.5 L6 6.5 L11 2.5"/></svg>
      brianne@crestmoorwm.example
    </li>
    <li>
      <svg viewBox="0 0 12 12"><circle cx="6" cy="6" r="5"/><ellipse cx="6" cy="6" rx="2.2" ry="5"/><line x1="1" y1="6" x2="11" y2="6"/></svg>
      www.crestmoorwm.example
    </li>
  </ul>

  <div class="rule"></div>
  <p class="address">20537 W. Harwell Pkwy Ste. B Larkmere, Nv 77512</p>
</section>

<section class="card card--back">
  <div class="brand">
    <span class="brand__mark"></span>
    <span class="brand__name">Crestmoor</span>
    <span class="brand__sub">Wealth Management</span>
  </div>
  <p class="web">www.<strong>crestmoorwealthmanagement</strong>.example</p>
</section>

</body>
</html>
```